Cordial Keys

We teach men how to be successful with women.

We will be putting an Vidhostly on the page.

We want to push men to take our 12 month learning program.

Open to ideas and layouts. The website will also be a landing page for our TV campaign.

Cordial keys is a company that will be marketing as an infomercial on late night television and via the internet. 

We will be selling a 12 month program for $997 (paid monthly). It will teach men how to get the woman of their dreams and how attraction is not a choice.
We have systematically developed a program for helping men attract women. 
We do have some competitors but they in the pickup commuinity (Hob Board, Greg Tolliver and Quillon Methods are all competitors.
Our website name is cordialkeys.com.au.
We will be having an vidhostly.com.au on our website to aid the process on making the sale.

The program will be an e-learning program that will be purchased over 12 months.

We also will be selling boot camps in which guys go for a week at a time and train to refine their skills.

Tv

```html
<!DOCTYPE html>
<html lang="en">
<head>
<meta charset="utf-8">
<title>Cordial Keys</title>
<link href="https://fonts.googleapis.com/css2?family=Roboto:wght@400;500;700&display=swap" rel="stylesheet">
<style>
:root{
  --page:#f8f8f8;
  --ink:#111;
  --text:#444;
  --muted:#666;
  --dark:#343434;
  --pink:#cc0099;
  --pink-light:#e455bd;
  --line:#bcbcbc;
  --cream:#fbf1dc;
  --gold:#d9c89a;
  --orange:#f08a1c;
}
*{margin:0;padding:0;box-sizing:border-box}
html,body{width:1200px;height:900px;overflow:hidden;background:var(--page)}
body{position:relative;font-family:'Roboto',sans-serif;color:var(--ink)}
.abs{position:absolute}

.masthead{left:108px;top:36px;width:988px;height:85px}
.brand{left:155px;top:56px;color:#fff;font-weight:500;font-size:28px;line-height:24px;text-align:right;width:198px}
.social{right:104px;top:30px;display:flex;gap:7px}
.social span{width:25px;height:25px;border-radius:3px;background:linear-gradient(#d8d8d8,#8a8a8a);display:block}
.callus{right:114px;top:87px;color:#fff;font-weight:700;font-size:18px}

.nav{left:108px;top:135px;width:988px;height:60px;background:#fff;border:1px solid #d6d6d6;border-radius:6px;box-shadow:0 2px 4px rgba(0,0,0,.12);overflow:hidden;white-space:nowrap}
.nav a{position:absolute;top:0;height:58px;line-height:58px;font-size:20px;color:var(--text);text-decoration:none}
.nav .current{left:0;width:163px;padding-left:18px;text-align:center;color:#fff;background:linear-gradient(var(--pink-light),var(--pink) 50%,#b8008a)}

.hero-panel{left:107px;top:216px;width:989px;height:320px;border-radius:8px;background:linear-gradient(#e9e9e9,#f8f8f8 45%,var(--page))}
.hero-title{left:169px;top:290px;font-size:30px;font-weight:700;white-space:nowrap}
.hero-copy{left:173px;top:340px;width:378px;font-size:13px;font-weight:700;line-height:18px;color:var(--text)}
.cta{left:169px;top:461px;width:181px;height:42px;border-radius:5px;background:linear-gradient(var(--pink-light),var(--pink) 50%,#b3008a);color:#fff;font-weight:700;font-size:18px;line-height:42px;text-align:center;text-decoration:none}

.laptop{left:575px;top:248px;width:521px;height:286px}
.laptop .screen{position:absolute;left:63px;top:0;width:395px;height:258px;background:#151515;border-radius:8px 8px 0 0;padding:13px 12px 12px}
.laptop .screen div{width:100%;height:100%;background:linear-gradient(135deg,#5c6b78,#a7b3bc 45%,#707d88)}
.laptop .base{position:absolute;left:0;top:257px;width:521px;height:27px;border-radius:2px 2px 12px 12px;background:linear-gradient(#f4f4f4,#c9c9c9)}

.offer{left:994px;top:478px;width:104px;height:104px}

.steps-title{left:310px;top:551px;font-size:19px;font-weight:700;letter-spacing:3.4px}
.step{width:118px;height:118px;border-radius:50%;background:radial-gradient(circle at 40% 30%,#fff 0,var(--cream) 45%,#efdcb2 100%);border:3px solid var(--gold);box-shadow:0 6px 6px rgba(0,0,0,.08)}
.step p{position:absolute;left:0;right:0;text-align:center;font-weight:500;color:var(--ink);line-height:1}
.step b{color:var(--pink);font-weight:500}
.step .num{position:absolute;right:14px;bottom:2px;width:20px;height:16px;background:#fff;color:var(--orange);font-size:11px;text-align:center;line-height:16px;border-radius:2px}

.perks{left:266px;top:731px;font-size:11px;color:#222;display:flex;gap:8px;align-items:center}
.perks svg{vertical-align:-2px;margin-right:2px}

.features{left:830px;top:578px;width:252px;list-style:none}
.features li{position:relative;height:46px;border-bottom:1px dotted #bbb;text-align:right;font-size:20px;line-height:38px}
.features li:last-child{border:none}
.features li::before{content:"";position:absolute;left:7px;top:18px;width:17px;height:14px;background:#ccc}
.features li::after{content:"";position:absolute;left:11px;top:22px;border:4.5px solid transparent;border-top:6px solid #fff}

.footer{left:98px;top:806px;width:989px;height:47px;border-top:1px solid #999;border-bottom:1px solid #999}
.footer-links{position:absolute;left:15px;top:11px;font-size:14px;color:var(--text);white-space:nowrap}
.footer-links a{color:var(--text);text-decoration:none}
.footer-links span{margin:0 11px 0 9px}
.copyright{position:absolute;right:0;top:15px;font-size:10.5px;color:var(--muted)}
</style>
</head>
<body>

<svg class="abs masthead" viewBox="0 0 988 85" aria-hidden="true">
  <path d="M0 12Q0 0 12 0H268Q278 0 284 10L300 39H976Q988 39 988 51V73Q988 85 976 85H12Q0 85 0 73Z" fill="#2f2f2f"/>
  <path d="M300 39H976Q988 39 988 51V58Q640 100 310 52Z" fill="#444"/>
</svg>
<div class="abs brand">Cordialkeys<br>.com</div>
<div class="abs social" aria-label="Social links"><span></span><span></span><span></span><span></span></div>
<div class="abs callus">Call us 99 555 123 40</div>

<nav class="abs nav">
  <a class="current" href="#">Home</a>
  <a href="#" style="left:246px">Aboutus</a>
  <a href="#" style="left:445px">Learning system</a>
  <a href="#" style="left:719px">Help</a>
  <a href="#" style="left:854px">Contact us</a>
</nav>

<div class="abs hero-panel"></div>
<h1 class="abs hero-title">We can help you !</h1>
<p class="abs hero-copy">Lorem ipsum dolor sit amet, consectetuer adipiscing elit. Aenean commodo ligula eget dolor. Aenean massa. Cum sociis natoque penatibus et magnis dis parturient montes, nascetur ridiculus mus. Donec quam felis, ultricies nec, pellentesque eu, pretium quis, sem. Nulla consequat massa quis enim. Donec pede justo</p>
<a class="abs cta" href="#">Get Started now</a>

<div class="abs laptop" role="img" aria-label="Laptop showing the program video with a woman's portrait behind cracked glass">
  <div class="screen"><div></div></div>
  <div class="base"></div>
</div>

<svg class="abs offer" viewBox="0 0 104 104">
  <polygon fill="#d0009a" points="52,2 58,12 68,5 71,17 82,13 81,25 94,25 89,36 100,40 92,49 101,57 91,63 97,74 85,76 87,88 75,87 73,99 63,94 56,103 49,94 40,101 35,90 24,94 23,82 11,81 15,70 4,64 13,56 3,48 14,42 8,31 20,29 18,17 30,19 32,7 43,12"/>
  <text x="52" y="50" fill="#fff" font-family="Roboto,sans-serif" font-weight="700" font-size="18" text-anchor="middle">SPECIAL</text>
  <text x="52" y="68" fill="#fff" font-family="Roboto,sans-serif" font-weight="700" font-size="18" text-anchor="middle">OFFER</text>
</svg>

<div class="abs steps-title">Easy Steps</div>
<svg class="abs" style="left:250px;top:560px" width="250" height="40" viewBox="0 0 250 40" aria-hidden="true">
  <path d="M34 5Q16 8 12 28" fill="none" stroke="#111" stroke-width="1.5"/>
  <path d="M7 24L12 35L17 24Z" fill="#111"/>
  <path d="M212 5Q230 8 235 28" fill="none" stroke="#111" stroke-width="1.5"/>
  <path d="M230 24L235 35L240 24Z" fill="#111"/>
</svg>

<div class="abs step" style="left:166px;top:598px">
  <p style="top:28px;font-size:17px">Choose</p>
  <p style="top:46px;font-size:14px">your <b style="font-size:22px">type</b></p>
  <p style="top:69px;font-size:9px">television / internet.</p>
  <span class="num">1</span>
</div>
<div class="abs step" style="left:324px;top:598px">
  <p style="top:26px;font-size:17px">Learning</p>
  <p style="top:44px;font-size:17px">program</p>
  <p style="top:60px;font-size:14px">with <b style="font-size:26px">us</b></p>
  <span class="num">2</span>
</div>
<div class="abs step" style="left:478px;top:598px">
  <p style="top:22px;font-size:17px;text-align:left;padding-left:25px">Get</p>
  <p style="top:41px;font-size:18px"><b>Matched</b></p>
  <p style="top:61px;font-size:13px">to Quality</p>
  <span class="num">3</span>
</div>

<div class="abs perks">
  <span><svg width="12" height="12" viewBox="0 0 12 12"><rect x="0.5" y="2.5" width="9" height="9" fill="#fff" stroke="#123a6b"/><path d="M2 6L5 9L11 1" fill="none" stroke="#123a6b" stroke-width="1.8"/></svg>Easy Service</span>
  <span>|</span>
  <span><svg width="12" height="12" viewBox="0 0 12 12"><rect x="0.5" y="2.5" width="9" height="9" fill="#fff" stroke="#123a6b"/><path d="M2 6L5 9L11 1" fill="none" stroke="#123a6b" stroke-width="1.8"/></svg>No Obligation</span>
  <span>|</span>
  <span><svg width="12" height="12" viewBox="0 0 12 12"><rect x="0.5" y="2.5" width="9" height="9" fill="#fff" stroke="#123a6b"/><path d="M2 6L5 9L11 1" fill="none" stroke="#123a6b" stroke-width="1.8"/></svg>Easy to use</span>
</div>

<ul class="abs features">
  <li>Find Single</li>
  <li>Fast &amp; easy Showings</li>
  <li>Simple to use</li>
  <li>Save time</li>
  <li>Reports &amp; feedback</li>
</ul>

<footer class="abs footer">
  <div class="footer-links"><a href="#">Home</a><span>|</span><a href="#">Aboutus</a><span>|</span><a href="#">Learning system</a><span>|</span><a href="#">Help</a><span>|</span><a href="#">Contact</a></div>
  <div class="copyright">Copyright © 2012 cordialkeys.com All rights reserved.</div>
</footer>

</body>
</html>
```